AMBER HARBOUR WEB

We need a home design in wordpress, we have now a web but we would like to improve it. Our current web is www.amberharbourvillas.example Our business is holliday rental of villas in Ibiza. Our guest must know that we are a reliable company, professional and with experience and good reviews. We want them to click in our reservation engine: https://bookings.amberharbourvillas.example/en/ and make reservation in our website. We would also like to say that all the properties that we have are just us who commercialize so we have best price available. Many people are going to see our villas in staylodgr.example and look to our website to make a reservation with us so we need to show them that they are at the right place and click at our link to our reservation engine. What make us special is that we are a local company, we are from Ibiza, Our guests are always received in person by the Amber Harbour Villas team. You will enjoy extensive tourist information when you check in and during the entire stay. You will be attended by ChatPelt and calls, always happy to help so that you have a happy and fun stay! Our guest stay is better than in hotel as they have more spece, private swiming pool, private garden, barbeque ... To rent a villa is the best way to stay in Ibiza. We also have a promotional video: https://vidshare.example/Qm7pTz3RxLa Let our philosophy be shown, we think that coming on holiday to Ibiza implies seeing the nature that we have in Ibiza, hence our name AMBER HARBOUR, like the pins that almost touch the sea in Ibiza, or the posidonea meadows where the intense green of the seaweed and the blue of the sea. We are aware of the environment, and we love Ibiza. For us, the client who visits Ibiza, should rent a car, go around the island, eat in a restaurant one day in front of the sea, is a night of partying to the discs, go shopping, visit the ancient heritage of Umanity, make some aquatic sport, enjoy the pool, those are for us Ibiza.

Target Market(s)

Europe, people from Holand, UK, Germany, France, Spain ...

Industry/Entity Type

Tourism

Colors

Designer to choose colors to be used in the design.

Requirements
Must have
• Pictures of Ibiza.
Nice to have
• Our name Amber Harbour Villas is beacuse in Ibiza there is forest that almost touch the watter of the Mediterranean sea, so you can see green of the forest and blue of the sea and the sky. And also beacause under the watter of the sea there is a plant called Posidonia that is also green please see the picture of posidonia.

```html
<!DOCTYPE html>
<html lang="en">
<head>
<meta charset="utf-8">
<title>Amber Harbour Villas – Home</title>
<link rel="stylesheet" href="https://fonts.googleapis.com/css2?family=Cinzel:wght@400;600;700&family=Open+Sans:wght@400;600;700&display=swap">
<style>
:root{
  --green:#5b7b2c;
  --green-dark:#486423;
  --leaf:#7aa83a;
  --blue:#2f9ad6;
  --sea:#1f6f93;
  --ink:#3a3a3a;
  --muted:#7b7b7b;
  --line:#e3e3e3;
  --soft:#f2f2f2;
  --white:#ffffff;
  --star:#f0a81c;
  --sun:#f3c623;
}
*{box-sizing:border-box;margin:0;padding:0}
html,body{width:1200px;height:4588px;overflow:hidden}
body{font-family:"Open Sans",Arial,sans-serif;color:var(--ink);background:var(--white);font-size:13px;line-height:1.6}
.heading{font-family:"Cinzel",Georgia,serif;font-weight:700;color:var(--green);text-align:center;letter-spacing:1px}
.btn{display:inline-block;background:var(--green);color:var(--white);font-size:12px;font-weight:600;padding:9px 22px;text-transform:uppercase;letter-spacing:.5px}
.wordmark{font-family:"Cinzel",Georgia,serif;font-weight:700;color:var(--green);display:flex;align-items:center;gap:8px}
.wordmark .dot{width:22px;height:22px;border-radius:50%;background:var(--green)}

/* header + hero */
.hero{position:relative;height:608px}
.hero-photo{position:absolute;inset:0;background:linear-gradient(180deg,#7fb3cf 0%,#3b8aa8 45%,#2d6c5a 70%,#3f6a38 100%)}
.site-header{position:absolute;top:0;left:0;right:0;height:80px;background:rgba(255,255,255,.92);display:flex;align-items:center;padding:0 60px}
.site-header .wordmark{font-size:20px}
.main-nav{display:flex;gap:26px;margin-left:auto;margin-right:24px;font-size:11px;font-weight:600;text-transform:uppercase;color:var(--ink)}
.main-nav .active{color:var(--green);border-bottom:2px solid var(--green)}
.header-btn{font-size:10px;padding:7px 16px;margin-left:8px}
.header-btn.blue{background:var(--blue)}
.lang{width:20px;height:14px;background:#c8102e;margin-left:14px}
.hero-title{position:absolute;top:262px;left:0;right:0;text-align:center;font-family:"Cinzel",Georgia,serif;font-weight:700;color:var(--white);font-size:46px;line-height:1.2;text-shadow:0 2px 8px rgba(0,0,0,.35)}
.search{position:absolute;left:140px;right:140px;top:566px;height:82px;background:var(--white);box-shadow:0 4px 14px rgba(0,0,0,.15);display:flex;align-items:flex-end;gap:14px;padding:0 20px 16px}
.field label{display:block;font-size:11px;color:var(--ink);margin-bottom:4px}
.field .box{height:30px;border:1px solid var(--line);font-size:10px;color:var(--muted);display:flex;align-items:center;padding:0 8px;gap:6px}
.field .box i{width:10px;height:10px;background:var(--blue);display:block}
.search .btn{margin-left:auto;padding:8px 20px}

/* about */
.about{position:relative;height:560px;padding:120px 140px 0}
.about-text{width:480px}
.about-text h2{display:flex;align-items:center;gap:10px;font-family:"Cinzel",Georgia,serif;color:var(--green);font-size:24px;margin-bottom:16px}
.about-text h2 span.logo{font-size:18px}
.about-text p{font-size:11px;color:var(--muted);margin-bottom:10px}
.about-photo{position:absolute;right:170px;top:110px;width:250px;height:400px;border-radius:46% 54% 40% 60%/35% 35% 65% 65%;background:linear-gradient(170deg,#2aa0c6 0%,#58b6cc 40%,#e7dcc0 70%,#4c7a3c 100%)}

/* amenities */
.amenities{height:560px;background:var(--soft);padding:70px 140px 0}
.amenities .heading{font-size:24px;margin-bottom:30px}
.amen-row{display:flex;height:370px}
.amen-photo{width:400px;background:linear-gradient(160deg,#6fa9d8 0%,#3a8fc4 45%,#e8e0d0 75%,#8a6f4e 100%)}
.amen-list{flex:1;background:var(--white);display:flex;flex-direction:column;padding:30px 0 0}
.amen-grid{display:grid;grid-template-columns:1fr 1fr;gap:22px 30px;padding:0 30px;flex:1}
.amen-item{display:flex;align-items:center;gap:10px;font-size:12px;color:var(--ink)}
.amen-item svg{flex:none}
.amen-list .btn{display:block;text-align:center;padding:14px;font-size:14px;margin:0 30px 20px}

/* video */
.videos{position:relative;height:620px;margin-top:20px}
.videos-bg{position:absolute;inset:0;background:linear-gradient(180deg,#2b2a27 0%,#3d3a34 60%,#ffffff 60%)}
.videos .heading{position:relative;color:var(--white);font-size:24px;padding-top:60px}
.videos .sub{position:relative;color:#d8d8d8;text-align:center;font-size:11px;width:620px;margin:8px auto 0}
.video-frame{position:absolute;left:290px;top:210px;width:620px;height:370px;background:linear-gradient(180deg,#d7e8f2 0%,#f1ece2 45%,#2aa3d0 80%,#1c86b6 100%);box-shadow:0 8px 20px rgba(0,0,0,.25)}
.play{position:absolute;left:50%;top:50%;transform:translate(-50%,-50%)}
.arrow-btn{position:absolute;top:310px;width:40px;height:40px;background:var(--blue);display:flex;align-items:center;justify-content:center}
.arrow-btn.prev{left:246px}.arrow-btn.next{right:246px}

/* gallery */
.gallery{height:640px;padding:40px 140px 0}
.gallery .heading{font-size:24px;margin-bottom:30px}
.gallery-grid{display:grid;grid-template-columns:repeat(4,1fr);grid-template-rows:repeat(2,190px);gap:10px}
.g{position:relative}
.g1{background:linear-gradient(160deg,#7cb0d8,#c9b891 60%,#7a6b49)}
.g2{background:linear-gradient(160deg,#3a6e34,#2fa3cf 70%,#d3c7ac)}
.g3{background:rgba(47,154,214,.88);color:var(--white);display:flex;flex-direction:column;align-items:center;justify-content:center;text-align:center;font-size:11px;padding:20px}
.g3 p{margin-top:8px}
.g4{background:linear-gradient(160deg,#8a5b34,#c6935c 60%,#e5d3b8)}
.g5{background:linear-gradient(160deg,#a57448,#d8b683 60%,#6f8a4a)}
.g6{background:linear-gradient(160deg,#4f8ac4,#f0e7d4 50%,#2e9fd0)}
.g7{background:linear-gradient(160deg,#6ea5d6,#7a9c54 50%,#2ea9d6)}
.g8{background:linear-gradient(160deg,#8fc0e0,#e9e1cf 55%,#2aa5d4)}
.gallery .more{display:block;width:110px;margin:30px auto 0;text-align:center;padding:8px 0;font-size:11px}

/* band */
.band{position:relative;height:300px;margin-top:12px}
.band-bg{position:absolute;inset:0;background:linear-gradient(180deg,#1f3c52 0%,#2a5a72 50%,#16303f 100%)}
.band-inner{position:relative;text-align:center;padding-top:80px}
.band h2{font-family:"Cinzel",Georgia,serif;color:var(--white);font-size:28px;line-height:1.3;font-weight:700}
.band .btn{margin-top:22px}

/* testimonials */
.testimonials{height:560px;padding:70px 140px 0}
.testimonials .heading{font-size:24px;margin-bottom:40px}
.t-row{display:flex;justify-content:center;align-items:center;gap:0;position:relative}
.t-card{width:300px;padding:22px;font-size:11px;color:#b0b0b0;font-style:italic;text-align:center}
.t-card.main{background:var(--white);box-shadow:0 4px 18px rgba(0,0,0,.15);color:var(--ink);font-style:normal;z-index:1;padding:30px 24px}
.stars{color:var(--star);font-size:14px;letter-spacing:2px;margin-top:8px}
.t-person{text-align:center;margin-top:30px}
.avatar{width:74px;height:74px;border-radius:50%;background:#c8d2d8;border:3px solid var(--white);box-shadow:0 2px 6px rgba(0,0,0,.2);margin:0 auto}
.t-person .name{font-family:"Cinzel",Georgia,serif;font-size:13px;color:var(--ink);margin-top:8px}

/* newsletter */
.newsletter{position:relative;height:330px;margin-top:40px;overflow:hidden;background:linear-gradient(100deg,#2d93d2 0%,#3aa6c8 55%,#7cc04a 100%)}
.newsletter h2{position:absolute;left:140px;top:70px;font-family:"Cinzel",Georgia,serif;color:var(--white);font-size:28px;font-weight:700}
.newsletter p{position:absolute;left:140px;top:116px;width:440px;color:#eaf6fb;font-size:11px}
.nl-form{position:absolute;left:140px;top:190px;display:flex}
.nl-form .input{width:300px;height:36px;background:var(--white);font-size:10px;color:var(--muted);display:flex;align-items:center;padding:0 12px}
.nl-form .btn{height:36px;padding:0 22px;display:flex;align-items:center;background:var(--green-dark)}
.nl-art{position:absolute;right:0;top:0;width:540px;height:330px;background:linear-gradient(180deg,rgba(124,192,74,0) 0%,rgba(243,198,35,.35) 100%)}

/* footer */
.site-footer{height:318px;padding:50px 140px 0;position:relative}
.f-cols{display:flex;gap:50px}
.f-col h4{font-family:"Cinzel",Georgia,serif;font-size:12px;color:var(--ink);margin-bottom:12px;font-weight:700}
.f-col ul{list-style:none;font-size:11px;color:var(--muted)}
.f-col li{margin-bottom:6px}
.f-col li::before{content:"›";color:var(--green);margin-right:6px}
.contact li::before{content:none}
.contact li{display:flex;gap:8px;align-items:center}
.contact li i{width:10px;height:10px;border-radius:50%;background:var(--green);display:block;flex:none}
.map{width:200px;height:110px;background:linear-gradient(135deg,#e8ecdf,#d7e3ee)}
.f-brand{margin-left:auto;text-align:center}
.f-brand .wordmark{font-size:18px}
.socials{display:flex;gap:6px;justify-content:center;margin-top:14px}
.socials span{width:22px;height:22px;background:var(--blue);display:block}
.copyright{position:absolute;left:0;right:0;bottom:0;height:40px;background:var(--green);color:var(--white);font-size:10px;display:flex;align-items:center;justify-content:center}
</style>
</head>
<body>

<section class="hero">
  <div class="hero-photo" role="img" aria-label="Turquoise Ibiza cove with pine-covered cliffs and a sandy beach"></div>
  <header class="site-header">
    <div class="wordmark"><span class="dot"></span>Amber Harbour</div>
    <nav class="main-nav">
      <span class="active">Home</span><span>Experience</span><span>About Us</span><span>Contact Us</span>
    </nav>
    <span class="btn header-btn blue">All Properties</span>
    <span class="btn header-btn">Book Now</span>
    <span class="lang"></span>
  </header>
  <h1 class="hero-title">The Best Way To Stay<br>In Ibiza!</h1>
  <form class="search">
    <div class="field"><label>Check in and out date</label><div class="box" style="width:220px"><i></i>Select check-in and out dates</div></div>
    <div class="field"><label>Nights</label><div class="box" style="width:60px">– 1 +</div></div>
    <div class="field"><label>No. of guests and rooms</label><div class="box" style="width:180px"><i></i>2 adults, 1 room</div></div>
    <div class="field"><label>Promo Code</label><div class="box" style="width:130px"><i></i>Enter</div></div>
    <span class="btn">Search</span>
  </form>
</section>

<section class="about">
  <div class="about-text">
    <h2>About <span class="logo wordmark"><span class="dot"></span>Amber Harbour</span></h2>
    <p>Amber Harbour Villas is a local company from Ibiza specialised in offering the best holiday accommodation in villas on the countryside of Ibiza. Our guests enjoy the rural island, tranquillity, views, private pools, close to the beaches and towns, the best restaurants, an unforgettable holiday for family or friends.</p>
    <p>Every day we live a different experience: beach, restaurant, flea market, disco, hiking, kayaking, boat trips, shopping, fishing, sunset with friends... a life of variety for all budgets.</p>
    <p>The maximum distance of the island are 41 kilometres from north to south and 15 kilometres from east to west; we always recommend renting a car. Enjoy the freedom to go where you prefer, without depending on schedules or public transportation.</p>
    <span class="btn" style="margin-top:8px">Read More</span>
  </div>
  <div class="about-photo" role="img" aria-label="Aerial view of a turquoise beach framed by green pine trees"></div>
</section>

<section class="amenities">
  <h2 class="heading">Our Amenities</h2>
  <div class="amen-row">
    <div class="amen-photo" role="img" aria-label="Villa terrace with sun loungers beside a private pool"></div>
    <div class="amen-list">
      <div class="amen-grid">
        <div class="amen-item"><svg width="26" height="26" viewBox="0 0 26 26"><circle cx="13" cy="13" r="12" fill="none" stroke="#2f9ad6" stroke-width="1.5"/><rect x="7" y="11" width="12" height="6" rx="2" fill="#2f9ad6"/></svg>Rent A Car</div>
        <div class="amen-item"><svg width="26" height="26" viewBox="0 0 26 26"><circle cx="13" cy="13" r="12" fill="none" stroke="#2f9ad6" stroke-width="1.5"/><path d="M7 13h12M13 7v12" stroke="#2f9ad6" stroke-width="2"/></svg>Go Around The Island</div>
        <div class="amen-item"><svg width="26" height="26" viewBox="0 0 26 26"><circle cx="13" cy="13" r="12" fill="none" stroke="#2f9ad6" stroke-width="1.5"/><rect x="8" y="10" width="10" height="9" fill="#2f9ad6"/></svg>Go Shopping</div>
        <div class="amen-item"><svg width="26" height="26" viewBox="0 0 26 26"><circle cx="13" cy="13" r="12" fill="none" stroke="#2f9ad6" stroke-width="1.5"/><path d="M9 7v12M17 7v12" stroke="#2f9ad6" stroke-width="2"/></svg>Eat In A Restaurant</div>
        <div class="amen-item"><svg width="26" height="26" viewBox="0 0 26 26"><circle cx="13" cy="13" r="12" fill="none" stroke="#2f9ad6" stroke-width="1.5"/><path d="M6 15q3-3 7 0t7 0" fill="none" stroke="#2f9ad6" stroke-width="2"/></svg>Aquatic Sport</div>
        <div class="amen-item"><svg width="26" height="26" viewBox="0 0 26 26"><circle cx="13" cy="13" r="12" fill="none" stroke="#2f9ad6" stroke-width="1.5"/><circle cx="13" cy="13" r="4" fill="#2f9ad6"/></svg>Night Of Partying To The Discos</div>
        <div class="amen-item"><svg width="26" height="26" viewBox="0 0 26 26"><circle cx="13" cy="13" r="12" fill="none" stroke="#2f9ad6" stroke-width="1.5"/><path d="M6 16q3-2 7 0t7 0M6 12q3-2 7 0t7 0" fill="none" stroke="#2f9ad6" stroke-width="1.5"/></svg>Enjoy The Pool</div>
        <div class="amen-item"><svg width="26" height="26" viewBox="0 0 26 26"><circle cx="13" cy="13" r="12" fill="none" stroke="#2f9ad6" stroke-width="1.5"/><path d="M8 19V11l5-4 5 4v8z" fill="#2f9ad6"/></svg>Visit The Ancient Heritage Of Humanity</div>
      </div>
      <span class="btn">Book Now</span>
    </div>
  </div>
</section>

<section class="videos">
  <div class="videos-bg" role="img" aria-label="Dusky view of a white villa courtyard"></div>
  <h2 class="heading">Watch Videos</h2>
  <p class="sub">Discover our villas and the island in our short film, from quiet pine coves to sunny terraces, and see why guests return to us every summer for their holidays.</p>
  <div class="video-frame" role="img" aria-label="White Ibiza villa with a blue pool, video still">
    <svg class="play" width="60" height="60" viewBox="0 0 60 60"><circle cx="30" cy="30" r="28" fill="rgba(255,255,255,.35)" stroke="#fff" stroke-width="2"/><path d="M24 18l18 12-18 12z" fill="#fff"/></svg>
  </div>
  <div class="arrow-btn prev"><svg width="14" height="14" viewBox="0 0 14 14"><path d="M9 2L4 7l5 5" fill="none" stroke="#fff" stroke-width="2"/></svg></div>
  <div class="arrow-btn next"><svg width="14" height="14" viewBox="0 0 14 14"><path d="M5 2l5 5-5 5" fill="none" stroke="#fff" stroke-width="2"/></svg></div>
</section>

<section class="gallery">
  <h2 class="heading">Our Gallery</h2>
  <div class="gallery-grid">
    <div class="g g1" role="img" aria-label="Stone villa facade with arched windows"></div>
    <div class="g g2" role="img" aria-label="Pool surrounded by pine trees"></div>
    <div class="g g3">
      <svg width="24" height="24" viewBox="0 0 24 24"><circle cx="12" cy="12" r="11" fill="none" stroke="#fff" stroke-width="1.5"/><path d="M12 7v10M7 12h10" stroke="#fff" stroke-width="1.5"/></svg>
      <p>Sunny terrace view<br>from the upper villa</p>
    </div>
    <div class="g g4" role="img" aria-label="Wooden dining room interior"></div>
    <div class="g g5" role="img" aria-label="Covered porch with outdoor dining table"></div>
    <div class="g g6" role="img" aria-label="Pool deck with loungers"></div>
    <div class="g g7" role="img" aria-label="Long blue pool with green lawn"></div>
    <div class="g g8" role="img" aria-label="White villa beside a turquoise pool"></div>
  </div>
  <span class="btn more">View More</span>
</section>

<section class="band">
  <div class="band-bg" role="img" aria-label="Harbour bay at dusk with boats and wooded hills"></div>
  <div class="band-inner">
    <h2>Villas And The Countryside<br>The Best Option To Stay In Ibiza</h2>
    <span class="btn">Book Now</span>
  </div>
</section>

<section class="testimonials">
  <h2 class="heading">Client Testimonials</h2>
  <div class="t-row">
    <div class="t-card">“ A peaceful villa with a lovely pool and a warm welcome from the local team, who helped us plan each day on the island. ”<div class="stars">★★★★★</div></div>
    <div class="t-card main">“ The house was spotless and the garden was perfect for the kids. Every question we sent was answered within minutes, and the tips for beaches were excellent. We already booked again. ”<div class="stars">★★★★★</div></div>
    <div class="t-card">“ Best holiday we have had. Great value, quiet countryside and the sea only a short drive away from the terrace. ”<div class="stars">★★★★★</div></div>
  </div>
  <div class="t-person">
    <div class="avatar" role="img" aria-label="Guest portrait"></div>
    <div class="name">Marten Vosse</div>
  </div>
</section>

<section class="newsletter">
  <div class="nl-art" role="img" aria-label="Decorative artwork of a rising sun and a plane in flight"></div>
  <h2>Newsletter Sign Up</h2>
  <p>Join our list for early offers, new villas and local tips on the best beaches, markets and restaurants across the island each season.</p>
  <div class="nl-form"><span class="input">Enter your Email Address</span><span class="btn">Subscribe</span></div>
</section>

<footer class="site-footer">
  <div class="f-cols">
    <div class="f-col"><h4>Quick Links</h4><ul><li>Home</li><li>Experience</li><li>About us</li><li>Contact Us</li></ul></div>
    <div class="f-col contact"><h4>Contact Details</h4><ul>
      <li><i></i>Amber Harbour Villas</li>
      <li><i></i>Carrer del Port 7, Ibiza</li>
      <li><i></i>+34 611 482 905</li>
      <li><i></i>stay@amberharbourvillas.example</li></ul></div>
    <div class="f-col"><h4>Location Map</h4><div class="map" role="img" aria-label="Location map of the island"></div></div>
    <div class="f-brand">
      <div class="wordmark"><span class="dot"></span>Amber Harbour</div>
      <div class="socials"><span></span><span></span><span></span><span></span></div>
    </div>
  </div>
  <div class="copyright">Copyright © 2019 Amber Harbour Villas. All Rights Reserved.</div>
</footer>

</body>
</html>
```